Veltrano Strom GmbH webpage The online Business card of a master electrician

A clean, modern webpage on whitch i can show my clients what im capable of and where the future costumer can inform himself. I need a login page for costumers who are registred and an secound webpage where my stuff can login to report theyr labour.
I will post pictures before and after, put on some commercial and crossellimg informations.
The costumer should find my insta as well my twitter or snapchat accounts.

Update:
Our Services are, Installations, Renovations, Home Automation, CCTV, Telefon / VOIP, Networking / Network-Cabeling, Electrical Supervisioning

Target Market(s)

Private and business costumers

Industry/Entity Type

Electric Company

Number of Pages Required

5+ page

Font styles to use
Sans Serif
Other font styles liked:
• Zurich,

Colors

Designer to choose colors to be used in the design.

Requirements
Must have
• A Page Hero
• A Costumer and staff login page (2separate pages)
• Contact form
• Responsive form
• Photo feed enbedding account veltrano_strom
Nice to have
• A Blog

```html
<!DOCTYPE html>
<html lang="en">
<head>
<meta charset="utf-8">
<title>Veltrano Strom GmbH</title>
<link href="https://fonts.googleapis.com/css2?family=Open+Sans:wght@400;600;700&display=swap" rel="stylesheet">
<style>
:root{
  --blue:#1552a8;
  --ink:#2b2b2b;
  --text:#555;
  --line:#d9d9d9;
  --topbar:#2e2e2e;
  --footer:#2f2f2f;
  --footer-base:#262626;
  --white:#fff;
}
*{box-sizing:border-box;margin:0;padding:0}
html,body{width:1200px;height:2782px;overflow:hidden}
body{font-family:"Open Sans",Arial,sans-serif;color:var(--text);background:var(--white);position:relative}
a{color:inherit;text-decoration:none}
.container{width:1094px;margin:0 auto;position:relative}

/* top bar */
.topbar{height:36px;background:var(--topbar);color:#eee;font-size:14px}
.topbar .container{width:1160px;display:flex;justify-content:space-between;align-items:center;height:36px}
.social-mini{display:flex;height:36px}
.social-mini span{width:34px;height:36px;border-right:1px solid #444;display:flex;align-items:center;justify-content:center}
.social-mini span:first-child{border-left:1px solid #444}
.social-mini i{width:10px;height:10px;border-radius:50%;background:#ddd;display:block}
.top-contact{display:flex;gap:26px;align-items:center}
.top-contact span{display:flex;gap:8px;align-items:center}

/* header */
.header{height:76px;border-bottom:1px solid #eee}
.header .container{width:1160px;display:flex;justify-content:space-between;align-items:center;height:76px}
.brand{display:flex;align-items:center;gap:10px;font-weight:700;font-size:24px;color:var(--blue);letter-spacing:.5px}
.brand-mark{width:22px;height:22px;background:var(--blue)}
.nav{display:flex;gap:44px;font-size:15px;color:#666;height:76px;align-items:center}
.nav a{position:relative;height:76px;display:flex;align-items:center}
.nav a.active{color:var(--blue)}
.nav a.active::after{content:"";position:absolute;left:0;right:0;bottom:-1px;height:3px;background:var(--blue)}

/* hero */
.hero{height:450px;background:linear-gradient(160deg,#3d3a33 0%,#5a5142 35%,#2b2a26 60%,#6b5a3e 100%);position:relative}
.hero-caption{position:absolute;left:41px;top:153px;width:502px;height:150px;background:rgba(235,235,235,.86);border-left:4px solid var(--blue);padding:20px 24px}
.hero-caption h1{color:var(--blue);font-size:25px;font-weight:600;margin-bottom:10px}
.hero-caption p{font-size:14.5px;line-height:21px;color:#333}
.hero-dots{position:absolute;left:556px;bottom:10px;display:flex;gap:8px}
.hero-dots i{width:24px;height:4px;background:#fff;display:block}
.hero-dots i.on{background:var(--blue)}

/* section title */
.section-title{text-align:center;font-size:24px;font-weight:600;color:var(--ink);letter-spacing:.5px}
.section-title b{color:var(--blue);font-weight:600}
.title-rule{width:250px;margin:12px auto 0;border-top:2px solid #bbb;position:relative}
.title-rule::after{content:"";position:absolute;left:20px;right:20px;top:4px;border-top:1px solid #ccc}

/* services */
.services{padding-top:60px}
.service-row{display:flex;gap:28px;margin-top:36px}
.service-card{width:252px;height:315px;border:1px solid var(--line);text-align:center;padding:22px 20px 0}
.service-card svg{width:70px;height:70px}
.service-card h3{font-size:16px;font-weight:700;color:var(--ink);margin-top:24px}
.service-card .tick{width:52px;height:3px;background:var(--blue);margin:8px auto 12px}
.service-card p{font-size:13.5px;line-height:21px}
.btn{display:inline-flex;height:34px;margin-top:16px;font-size:14px;font-weight:600}
.btn .lbl{background:var(--ink);color:#fff;padding:0 20px;display:flex;align-items:center}
.btn .arr{background:var(--blue);color:#fff;width:34px;display:flex;align-items:center;justify-content:center}
.slide-arrow{position:absolute;top:135px;width:42px;height:42px;border:1px solid #ccc;background:#fff;display:flex;align-items:center;justify-content:center}
.slide-arrow.prev{left:-47px}
.slide-arrow.next{right:-47px}

/* welcome */
.welcome{padding-top:74px}
.welcome-body{display:flex;justify-content:space-between;margin-top:46px}
.welcome-text{width:640px;text-align:center;font-size:14px;line-height:24px;margin-left:16px}
.welcome-text h2{font-size:17px;font-weight:600;color:#444;line-height:26px;white-space:nowrap}
.welcome-text p{margin-bottom:24px}
.welcome-text p:last-child{margin-bottom:0}
.video-frame{width:405px;height:246px;border:1px solid var(--line);padding:10px;margin-top:19px}
.video{width:100%;height:100%;background:linear-gradient(180deg,#8aa07a 0%,#6f8f5a 45%,#9a9a94 100%)}

/* projects */
.projects{display:flex;justify-content:space-between;margin-top:82px}
.project-card{width:344px;height:407px;border:1px solid var(--line);padding:8px;text-align:center}
.project-img{height:182px}
.project-card h3{font-size:19px;font-weight:700;color:var(--ink);margin-top:18px;letter-spacing:.4px}
.project-card .tick{width:60px;height:3px;background:var(--blue);margin:8px auto 12px}
.project-card p{font-size:13.5px;line-height:21px;padding:0 6px}
.project-card .btn{margin-top:18px}

/* feed */
.feed{margin-top:102px;text-align:center}
.feed-title{display:inline-flex;align-items:center;gap:10px;font-size:24px;font-weight:600;color:var(--ink);height:36px}
.feed-title i{width:30px;height:30px;border-radius:50%;background:var(--blue);display:block}
.feed-grid{width:608px;margin:16px auto 0;display:grid;grid-template-columns:repeat(4,141px);gap:16px 14px}
.feed-grid div{height:125px}
.t-a{background:linear-gradient(135deg,#3b3f3a,#8b9188)}
.t-b{background:linear-gradient(135deg,#d8d4cc,#6b6257)}
.t-c{background:linear-gradient(135deg,#2a2624,#e9e6e1)}
.feed-btn{display:inline-flex;align-items:center;gap:8px;margin-top:14px;background:var(--blue);color:#fff;font-size:13px;font-weight:600;padding:0 14px;height:33px;border-radius:3px}
.feed-btn i{width:14px;height:14px;border:2px solid #fff;border-radius:3px;display:block}

/* footer */
.footer{position:absolute;left:0;right:0;top:2480px;bottom:0;background:var(--footer);border-top:5px solid var(--blue);color:#ccc}
.footer-cols{display:flex;width:1126px;margin:0 auto;padding-top:26px;height:245px}
.footer h4{color:#fff;font-size:16px;font-weight:700;letter-spacing:.5px}
.footer .tick{width:42px;height:3px;background:var(--blue);margin:8px 0 20px}
.f-contact{width:362px}
.f-contact li{list-style:none;display:flex;gap:14px;font-size:13.5px;line-height:19px;margin-bottom:17px}
.f-contact svg{flex:none;width:16px;height:16px;margin-top:2px}
.f-menu{width:460px}
.f-menu ul{display:grid;grid-template-columns:208px 200px;row-gap:14px;list-style:none;font-size:13px}
.f-menu li::before{content:"\2192";color:var(--blue);margin-right:12px}
.f-about{width:304px;text-align:center}
.f-about h4{text-align:left}
.f-about p{font-size:13.5px;line-height:21px}
.f-social{display:flex;gap:16px;justify-content:center;margin-top:18px}
.f-social i{width:12px;height:12px;border-radius:50%;background:#fff;display:block}
.copyright{position:absolute;left:0;right:0;bottom:0;height:52px;background:var(--footer-base);display:flex;align-items:center;justify-content:center;font-size:12px;color:#ddd}
.copyright b{color:var(--blue);font-weight:400;margin:0 3px}
</style>
</head>
<body>

<div class="topbar">
  <div class="container">
    <div class="social-mini"><span><i></i></span><span><i></i></span><span><i></i></span><span><i></i></span><span><i></i></span></div>
    <div class="top-contact">
      <span><svg width="14" height="14" viewBox="0 0 24 24" fill="#eee"><path d="M6.6 10.8a15 15 0 0 0 6.6 6.6l2.2-2.2c.3-.3.7-.4 1-.2 1.1.4 2.3.6 3.6.6.6 0 1 .4 1 1V20c0 .6-.4 1-1 1A17 17 0 0 1 3 4c0-.6.4-1 1-1h3.5c.6 0 1 .4 1 1 0 1.3.2 2.5.6 3.6.1.3 0 .7-.2 1z"/></svg>555 204 7318</span>
      <span><svg width="15" height="12" viewBox="0 0 24 18" fill="none" stroke="#eee" stroke-width="2"><rect x="1" y="1" width="22" height="16"/><path d="M1 1l11 9 11-9"/></svg>info@veltranostrom.ch</span>
    </div>
  </div>
</div>

<header class="header">
  <div class="container">
    <a class="brand"><span class="brand-mark"></span>VELTRANO STROM</a>
    <nav class="nav">
      <a class="active">HOME</a><a>ABOUT US</a><a>GALLERY</a><a>SERVICE</a><a>BLOG</a><a>CONTACT US</a>
    </nav>
  </div>
</header>

<section class="hero" role="img" aria-label="Photo of a restaurant interior with warm ceiling lights">
  <div class="hero-caption">
    <h1>LOREM IPSUM DOLOR SIT AMET...</h1>
    <p>Lorem Ipsum is simply dummy text of the printing and typesetting industry. Lorem Ipsum has been the industry's standard dummy text ever since the 1500s, when an unknown printer.</p>
  </div>
  <div class="hero-dots"><i></i><i class="on"></i><i></i></div>
</section>

<section class="services">
  <h2 class="section-title">OUR <b>SERVICE</b></h2>
  <div class="title-rule"></div>
  <div class="container">
    <div class="slide-arrow prev"><svg width="14" height="24" viewBox="0 0 14 24" fill="none" stroke="#333" stroke-width="2.5"><path d="M12 2L2 12l10 10"/></svg></div>
    <div class="slide-arrow next"><svg width="14" height="24" viewBox="0 0 14 24" fill="none" stroke="#333" stroke-width="2.5"><path d="M2 2l10 10L2 22"/></svg></div>
    <div class="service-row">
      <article class="service-card">
        <svg viewBox="0 0 64 64" fill="#444"><path d="M14 8l10 10-3 3 22 22 3-3 10 10-8 8-10-10 3-3-22-22-3 3L6 16z"/><rect x="36" y="10" width="8" height="26" transform="rotate(45 40 23)"/></svg>
        <h3>INSTALLATIONS</h3><div class="tick"></div>
        <p>Lorem ipsum dolor sit amet, consectetur adipiscing elit, sed do eiusmod tempor incididunt ut labore et dolore magna aliqua.</p>
        <a class="btn"><span class="lbl">Read More</span><span class="arr">»</span></a>
      </article>
      <article class="service-card">
        <svg viewBox="0 0 64 64" fill="none" stroke="#444" stroke-width="4"><path d="M8 32L32 10l24 22"/><path d="M16 28v24h32V28"/><rect x="27" y="38" width="10" height="14" fill="#444"/></svg>
        <h3>RENOVATIONS</h3><div class="tick"></div>
        <p>Lorem ipsum dolor sit amet, consectetur adipiscing elit, sed do eiusmod tempor incididunt ut labore et dolore magna aliqua.</p>
        <a class="btn"><span class="lbl">Read More</span><span class="arr">»</span></a>
      </article>
      <article class="service-card">
        <svg viewBox="0 0 64 64" fill="none" stroke="#444" stroke-width="4"><rect x="30" y="12" width="20" height="26" transform="rotate(35 40 25)"/><path d="M26 38c-10 0-16 6-16 14M10 52h8"/><path d="M48 12l6-6"/></svg>
        <h3>NETWORK-CABELING</h3><div class="tick"></div>
        <p>Lorem ipsum dolor sit amet, consectetur adipiscing elit, sed do eiusmod tempor incididunt ut labore et dolore magna aliqua.</p>
        <a class="btn"><span class="lbl">Read More</span><span class="arr">»</span></a>
      </article>
      <article class="service-card">
        <svg viewBox="0 0 64 64" fill="#444"><rect x="36" y="6" width="18" height="6"/><rect x="42" y="12" width="6" height="10"/><path d="M8 30l36-10 6 14-36 10z"/><circle cx="14" cy="38" r="4" fill="#fff"/><path d="M22 44l4 10h-8z"/></svg>
        <h3>CCTV</h3><div class="tick"></div>
        <p>Lorem ipsum dolor sit amet, consectetur adipiscing elit, sed do eiusmod tempor incididunt ut labore et dolore magna aliqua.</p>
        <a class="btn"><span class="lbl">Read More</span><span class="arr">»</span></a>
      </article>
    </div>
  </div>
</section>

<section class="welcome">
  <h2 class="section-title">WELCOME TO <b>VELTRANO STROM</b></h2>
  <div class="title-rule"></div>
  <div class="container welcome-body">
    <div class="welcome-text">
      <h2>Lorem Ipsum is simply dummy text of the printing and typesetting industry.</h2>
      <p>Lorem Ipsum has been the industry's standard dummy text ever since the 1500s, when an unknown printer took a galley of type and scrambled it to make a type specimen book.</p>
      <p>It has survived not only five centuries, but also the leap into electronic typesetting, remaining essentially unchanged. It was popularised in the 1960s with the release of transfer sheets containing Lorem Ipsum passages of Lorem Ipsum.</p>
      <p>Lorem ipsum dolor sit amet, consectetur adipiscing elit, sed do eiusmod tempor incididunt ut labore et dolore magna aliqua. Ut enim ad minim veniam, quis nostrud exercitation ullamco laboris nisi ut aliquip ex ea commodo consequat.</p>
    </div>
    <div class="video-frame"><div class="video" role="img" aria-label="Video still of two workers servicing equipment in a garden"></div></div>
  </div>

  <div class="container projects">
    <article class="project-card">
      <div class="project-img" role="img" aria-label="Photo of a restaurant dining room" style="background:linear-gradient(180deg,#6a2f2c 0%,#c9b79a 55%,#3a332c 100%)"></div>
      <h3>RESTAURANT</h3><div class="tick"></div>
      <p>Lorem ipsum dolor sit amet, consectetur adipiscing elit, sed do eiusmod tempor incididunt ut labore et dolore magna aliqua. Ut enim ad minim veniam, quis nostrud exercitation.</p>
      <a class="btn"><span class="lbl">READ MORE</span><span class="arr">»</span></a>
    </article>
    <article class="project-card">
      <div class="project-img" role="img" aria-label="Photo of a city riverside at dusk" style="background:linear-gradient(180deg,#3d5a86 0%,#b89a8a 50%,#2b3344 100%)"></div>
      <h3>RESIZED</h3><div class="tick"></div>
      <p>Lorem ipsum dolor sit amet, consectetur adipiscing elit, sed do eiusmod tempor incididunt ut labore et dolore magna aliqua. Ut enim ad minim veniam, quis nostrud exercitation.</p>
      <a class="btn"><span class="lbl">READ MORE</span><span class="arr">»</span></a>
    </article>
    <article class="project-card">
      <div class="project-img" role="img" aria-label="Aerial photo of a green village with houses" style="background:linear-gradient(180deg,#7f9a6a 0%,#a8a494 50%,#4d6b3c 100%)"></div>
      <h3>OAKHILL FUER BRAMWELL</h3><div class="tick"></div>
      <p>Lorem ipsum dolor sit amet, consectetur adipiscing elit, sed do eiusmod tempor incididunt ut labore et dolore magna aliqua. Ut enim ad minim veniam, quis nostrud exercitation.</p>
      <a class="btn"><span class="lbl">READ MORE</span><span class="arr">»</span></a>
    </article>
  </div>
</section>

<section class="feed">
  <div class="feed-title"><i></i>veltrano_strom</div>
  <div class="feed-grid">
    <div class="t-a" role="img" aria-label="Photo of a wired electrical cabinet"></div>
    <div class="t-b" role="img" aria-label="Photo of wiring before and after"></div>
    <div class="t-c" role="img" aria-label="Photo of a coffee cup on a saucer"></div>
    <div class="t-a" role="img" aria-label="Photo of a wired electrical cabinet"></div>
    <div class="t-c" role="img" aria-label="Photo of a coffee cup on a saucer"></div>
    <div class="t-a" role="img" aria-label="Photo of a wired electrical cabinet"></div>
    <div class="t-b" role="img" aria-label="Photo of wiring before and after"></div>
    <div class="t-c" role="img" aria-label="Photo of a coffee cup on a saucer"></div>
  </div>
  <a class="feed-btn"><i></i>View Photo feed</a>
</section>

<footer class="footer">
  <div class="footer-cols">
    <div class="f-contact">
      <h4>CONTACT</h4><div class="tick"></div>
      <ul>
        <li><svg viewBox="0 0 24 24" fill="#ddd"><path d="M12 1a8 8 0 0 0-8 8c0 6 8 14 8 14s8-8 8-14a8 8 0 0 0-8-8zm0 11a3 3 0 1 1 0-6 3 3 0 0 1 0 6z"/></svg><span>4217 Birch Hollow Rd Fairview,<br>CA 90210.</span></li>
        <li><svg viewBox="0 0 24 24" fill="#ddd"><path d="M6.6 10.8a15 15 0 0 0 6.6 6.6l2.2-2.2c.3-.3.7-.4 1-.2 1.1.4 2.3.6 3.6.6.6 0 1 .4 1 1V20c0 .6-.4 1-1 1A17 17 0 0 1 3 4c0-.6.4-1 1-1h3.5c.6 0 1 .4 1 1 0 1.3.2 2.5.6 3.6.1.3 0 .7-.2 1z"/></svg><span>555 204 7318</span></li>
        <li><svg viewBox="0 0 24 18" fill="none" stroke="#ddd" stroke-width="2"><rect x="1" y="1" width="22" height="16"/><path d="M1 1l11 9 11-9"/></svg><span>info@veltranostrom.ch</span></li>
        <li><svg viewBox="0 0 24 24" fill="none" stroke="#ddd" stroke-width="2"><circle cx="12" cy="12" r="10"/><path d="M2 12h20M12 2c3 3 3 17 0 20M12 2c-3 3-3 17 0 20"/></svg><span>www.veltranostrom.ch</span></li>
      </ul>
    </div>
    <div class="f-menu">
      <h4>MENU LINK</h4><div class="tick"></div>
      <ul>
        <li>HOME</li><li>ABOUT US</li>
        <li>GALLERY</li><li>SERVICE</li>
        <li>BLOG</li><li>CONTACT US</li>
        <li>PRIVACY POLICY</li><li>TERMS &amp; CONDITIONS</li>
      </ul>
    </div>
    <div class="f-about">
      <h4>ABOUT</h4><div class="tick"></div>
      <p>Lorem ipsum dolor sit amet, consectetur adipiscing elit, sed do eiusmod tempor incididunt ut labore et dolore magna aliqua. Ut enim ad minim veniam, quis nostrud exercitation ullamco laboris nisi ut aliquip ex ea commodo consequat.</p>
      <div class="f-social"><i></i><i></i><i></i><i></i><i></i></div>
    </div>
  </div>
  <div class="copyright">Copyright © 2017 <b>VeltranoStrom.ch</b>. All Rights Reserved</div>
</footer>

</body>
</html>
```